Brimstone Corporation Pty Ltd

Contruction industry
It's a wall and floor tiling business

Industry/Entity Type

Business

Requirements
Must have
• Likes-
- clean and easy to read
- a witty design is always well received
- for it to look reputable in the industry
- a strong and direct presentation
- simple but striking colour selection
Should not have
• Dislikes-
- pls no tacky square tiles to resemble tiling

```html
<!DOCTYPE html>
<html lang="en">
<head>
<meta charset="utf-8">
<title>Brimstone Corporation Pty Ltd — business card</title>
<link href="https://fonts.googleapis.com/css2?family=Lato:wght@400&display=swap" rel="stylesheet">
<style>
  :root {
    --page-bg: #e9e7e4;
    --card-blue: #0b2c9c;
    --card-ink: #ffffff;
    --card-edge: #0a0a0a;
    --rule: rgba(255,255,255,0.75);
  }
  * { margin: 0; padding: 0; box-sizing: border-box; }
  html, body {
    width: 1200px; height: 1023px; overflow: hidden;
    background: var(--page-bg);
    font-family: "Lato", Arial, sans-serif;
    font-weight: 400;
  }
  .card {
    position: absolute;
    left: 220px;
    width: 760px; height: 463px;
    background: var(--card-blue);
    border-radius: 18px;
    color: var(--card-ink);
    overflow: hidden;
    box-shadow: 0 10px 28px rgba(0,0,0,0.25);
  }
  .card--back { top: 30px; }
  .card--front { top: 530px; }

  /* back side */
  .card__edge-band {
    position: absolute; top: 0; left: 0; right: 0; height: 16px;
    background: var(--card-edge);
  }
  .back-name {
    position: absolute; left: 44px; top: 238px; width: 340px;
    text-align: right;
    font-size: 30px; line-height: 1.25;
  }
  .divider-vertical {
    position: absolute; left: 402px; top: 150px; width: 2px; height: 170px;
    background: var(--rule);
  }
  .divider-horizontal {
    position: absolute; left: 40px; top: 214px; width: 420px; height: 2px;
    background: linear-gradient(90deg, rgba(255,255,255,0) 0%, var(--rule) 70%, rgba(255,255,255,0) 100%);
  }
  .contact {
    position: absolute; left: 428px; top: 150px;
  }
  .contact__name { font-size: 46px; line-height: 1; margin-bottom: 26px; }
  .contact__row {
    display: flex; align-items: center; gap: 12px;
    font-size: 19px; line-height: 1; margin-bottom: 16px;
  }
  .contact__icon { width: 20px; height: 20px; flex: none; }

  /* front side */
  .front-name {
    position: absolute; left: 0; right: 0; top: 205px;
    text-align: center; white-space: nowrap;
    font-size: 42px; line-height: 1.2;
  }
</style>
</head>
<body>
  <section class="card card--back" aria-label="Card back">
    <div class="card__edge-band"></div>
    <div class="divider-horizontal"></div>
    <div class="divider-vertical"></div>
    <div class="back-name">Brimstone<br>Corporation Pty Ltd</div>
    <div class="contact">
      <div class="contact__name">Dan Morel</div>
      <div class="contact__row">
        <svg class="contact__icon" viewBox="0 0 24 24" aria-hidden="true">
          <path d="M6.6 10.8c1.4 2.8 3.8 5.1 6.6 6.6l2.2-2.2c.3-.3.7-.4 1-.2 1.1.4 2.3.6 3.6.6.6 0 1 .4 1 1V20c0 .6-.4 1-1 1C10.6 21 3 13.4 3 4c0-.6.4-1 1-1h3.5c.6 0 1 .4 1 1 0 1.3.2 2.5.6 3.6.1.3 0 .7-.2 1l-2.3 2.2z" fill="#ffffff"/>
        </svg>
        <span>0400 555 218</span>
      </div>
      <div class="contact__row">
        <svg class="contact__icon" viewBox="0 0 24 24" aria-hidden="true">
          <rect x="2" y="5" width="20" height="14" rx="2" fill="#ffffff"/>
          <path d="M3 6l9 7 9-7" fill="none" stroke="#0b2c9c" stroke-width="1.8"/>
        </svg>
        <span>dan.morel@mailbox.com</span>
      </div>
    </div>
  </section>

  <section class="card card--front" aria-label="Card front">
    <div class="front-name">Brimstone Corporation Pty Ltd</div>
  </section>
</body>
</html>
```